Need Responsive Email Newsletter Design

Looking for a clean, professional newsletter to send in our next email blast to our customers. Need a combination Graduation Gift and Father's Day theme for our briefcases and travel bags. "40% - 75% Off Storewide!" "Free Shipping On All Orders (No Minimum Required)!" "Make it extra special with a custom monogram!" Some sample photos are attached. Please, only top quality designers apply!
Updates
Logo and company can be found at Satchelry.com. Added Friday, May 8, 2015
Industry/Entity Type
It Professional
Look and feel
Each slider illustrates characteristics of the customer's brand and the style your logo design should communicate.

```html
<!DOCTYPE html>
<html lang="en">
<head>
<meta charset="utf-8">
<title>Satchelry.com Newsletter</title>
<link href="https://fonts.googleapis.com/css2?family=Arimo:wght@400;700&display=swap" rel="stylesheet">
<style>
:root{
  --green:#7bb32e;
  --btn:#80b43a;
  --text:#666;
  --title:#555;
  --muted:#888;
  --link:#667;
  --rule:#e6e6e6;
  --band:#f7f7f7;
  --white:#fff;
  --footer:#555;
  --ink:#3a3a3a;
  --sale:#d9261c;
  --leather-a:#6e3318;
  --leather-b:#a4562c;
  --red-a:#7d1420;
  --red-b:#b8303c;
}
*{box-sizing:border-box;margin:0;padding:0}
html,body{width:974px;height:1200px;overflow:hidden}
body{font-family:"Arimo",Arial,sans-serif;color:var(--text);background:var(--band);position:relative}
.column{width:490px;margin:0 auto}

.header{background:var(--white);height:166px;border-bottom:1px solid var(--rule)}
.topbar{height:14px;display:flex;justify-content:space-between;font-size:8px;color:var(--muted);padding-top:2px}
.brand{text-align:center;padding-top:6px;height:62px}
.brand-name{font-size:26px;font-weight:700;color:var(--ink);letter-spacing:.5px;display:inline-flex;align-items:center;gap:8px;line-height:28px}
.brand-mark{width:18px;height:18px;background:var(--ink);display:inline-block}
.brand-tag{font-size:6px;font-weight:700;color:var(--ink);letter-spacing:.3px;margin-top:2px}
.brand-sale{font-size:8px;font-weight:700;color:var(--sale);margin-top:1px}
.nav{border-top:1px solid var(--rule);width:360px;margin:4px auto 0;display:flex;justify-content:center;gap:22px;padding-top:5px;font-size:10px;color:var(--muted)}
.headline{color:var(--green);font-size:16.5px;font-weight:700;text-align:center;line-height:23px;margin-top:16px}

.intro{text-align:center;font-size:12.5px;font-weight:700;color:var(--muted);line-height:16px;padding-top:15px;height:63px}

.product{border-top:1px solid var(--rule);height:178px;display:flex;align-items:center}
.product-photo{width:136px;height:100px;margin-left:16px;border-radius:12px;flex:none}
.photo-leather{background:linear-gradient(160deg,var(--leather-b),var(--leather-a))}
.photo-red{background:linear-gradient(160deg,var(--red-b),var(--red-a))}
.product-body{margin-left:36px;width:280px}
.product-title{font-size:20px;line-height:24px;color:var(--title);text-align:center;font-weight:400;padding-bottom:10px;border-bottom:1px solid var(--rule);margin-bottom:10px}
.product-text{font-size:9.5px;line-height:14px;color:var(--muted)}
.button{display:block;width:129px;height:21px;margin:12px auto 0;background:var(--btn);color:var(--white);font-size:10px;text-align:center;line-height:21px;text-decoration:none}

.closing{border-top:1px solid var(--rule);color:var(--green);font-size:16.5px;font-weight:700;text-align:center;line-height:21px;padding:14px 10px 0;height:97px}

.contact{border-top:1px solid var(--rule);display:flex;padding:14px 0 0 8px;height:77px;font-size:9.5px}
.contact-list{list-style:none;width:207px}
.contact-list li{display:flex;align-items:center;gap:12px;height:15px;font-weight:700;color:var(--link)}
.contact-list a{color:var(--link)}
.contact-list svg{width:10px;height:10px;fill:var(--muted)}
.contact-note{width:250px;line-height:13px;color:var(--muted)}
.contact-note b{color:var(--link);text-decoration:underline}

.social{border-top:1px solid var(--rule);display:flex;justify-content:center;gap:20px;padding-top:18px;height:50px}
.social span{width:15px;height:15px;border-radius:50%;background:#aaa;display:block}

.footer{position:absolute;left:0;right:0;bottom:0;height:47px;background:var(--footer);color:var(--white);text-align:center;font-size:9.5px;line-height:15px;padding-top:8px}
</style>
</head>
<body>
<header class="header">
  <div class="column">
    <div class="topbar"><span>View online version</span><span>Issue Date: May 10, 2015</span><span>Subscribe | Forward</span></div>
    <div class="brand">
      <div class="brand-name"><span class="brand-mark"></span>Satchelry.com</div>
      <div class="brand-tag">PREMIUM BRIEFCASES AT VALUE PRICES SINCE 1966</div>
      <div class="brand-sale">24 HOUR SALE ENDS TONIGHT!</div>
    </div>
    <nav class="nav"><span>HOME</span><span>SALES</span><span>FAQ</span><span>CONTACT</span></nav>
    <h1 class="headline">Father's Day &amp; Graduation Gifts: 40% - 75% Off Storewide on Briefcases and Travel Bags</h1>
  </div>
</header>

<main class="column">
  <p class="intro">Free Shipping On All Orders (No Minimum Required)!<br>Make it extra special with a custom monogram on every gift bag</p>

  <section class="product">
    <div class="product-photo photo-leather" role="img" aria-label="Brown leather lady bag"></div>
    <div class="product-body">
      <h2 class="product-title">Satchelry.com Lady Bag</h2>
      <p class="product-text">Sed ut perspiciatis unde omnis iste natus error sit voluptatem accusantium doloremque laudantium, totam rem aperiam, eaque ipsa quae ab illo inventore veritatis et quasi architecto beatae vitae dicta sunt explicabo. Nemo enim ipsam voluptatem quia voluptas sit aut odit aut</p>
      <a class="button" href="#">READ MORE</a>
    </div>
  </section>

  <section class="product">
    <div class="product-photo photo-red" role="img" aria-label="Red leather hand bag"></div>
    <div class="product-body">
      <h2 class="product-title">Satchelry.com Hand Bag</h2>
      <p class="product-text">But I must explain to you how all this mistaken idea of denouncing pleasure and praising pain was born and I will give you a complete account of the system, and expound the actual</p>
      <a class="button" href="#">READ MORE</a>
    </div>
  </section>

  <section class="product">
    <div class="product-photo photo-leather" role="img" aria-label="Tan leather briefcase"></div>
    <div class="product-body">
      <h2 class="product-title">Satchelry.com Briefcase</h2>
      <p class="product-text">At vero eos et accusamus et iusto odio dignissimos ducimus qui blanditiis praesentium voluptatum deleniti atque corrupti quos dolores et quas molestias excepturi sint occaecati cupiditate non provident, similique sunt in culpa qui officia deserunt mollitia animi</p>
      <a class="button" href="#">VISIT OUR STORE</a>
    </div>
  </section>

  <section class="product">
    <div class="product-photo photo-leather" role="img" aria-label="Brown leather messenger case"></div>
    <div class="product-body">
      <h2 class="product-title">Satchelry.com unique</h2>
      <p class="product-text">Lorem Ipsum is simply dummy text of the printing and typesetting industry. Lorem Ipsum has been the industry's standard dummy text ever since the 1500s, Lorem Ipsum is simply dummy text of the printing and typesetting industry. Lorem Ipsum has been the ...</p>
      <a class="button" href="#">VISIT OUR STORE</a>
    </div>
  </section>

  <p class="closing">Make it extra special with a custom monogram! Free Shipping On All Orders, No Minimum Required, for Dad and the Graduate</p>

  <section class="contact">
    <ul class="contact-list">
      <li><svg viewBox="0 0 10 10"><path d="M5 1 0 5h1.5v4h2.5V6.5h2V9h2.5V5H10z"/></svg><a href="#">www.satchelry.com</a></li>
      <li><svg viewBox="0 0 10 10"><path d="M0 2h10v6H0zM1 3v.3L5 6l4-2.7V3z" fill-rule="evenodd"/></svg><a href="#">support@satchelry.com</a></li>
      <li><svg viewBox="0 0 10 10"><path d="M2 0 4 2.5 3 4q1 2 3 3l1.5-1L10 8 8.5 10Q4 9.5 0 2z"/></svg><span>(00 000) 22 333 44</span></li>
    </ul>
    <p class="contact-note">You are receiving this because you're a current subscriber, have bought from us.<br><b>Subscribe</b> to our list | <b>Unsubscribe</b> from this list</p>
  </section>

  <nav class="social" aria-label="Social links"><span></span><span></span><span></span><span></span><span></span><span></span></nav>
</main>

<footer class="footer">
  P.O. Box 00000, Satchelry, Lantern Falls NY 12345<br>
  <b>© Copyright satchelry 2015</b>
</footer>
</body>
</html>
```